Etikett für für Teigtaschen mit Käsefüllung
Zielgruppe
Ich bin Kleinunternehmerin und stelle Teigtaschen her.
Meine Zielgruppe sind Feinkostläden bzw. Endverbraucher
Aufgabenstellung
Ich übersende Ihnen erstmals eine Vorlage der Etikette für Teigtaschen mit Käsefülle.... je nach Fülle, sollte ein tolles Bild für die jeweilige Fülle - in diesem Fall 'Käse' erscheinen. Es sind ja mehrere Käsesorten in der Teigtasche enthalten. Meine LOGO-Daten sind bei Ihnen gespeichert.
Bei der Nährwerttabelle ändern sich noch die Angaben an Gramm....
Die restlichen fünf Banderolen werde ich Ihnen schnellstens nachmailen.
Ich habe keine besonderen Wünsche, deshalb vertraue ich Ihren Designern und bin schon auf die ersten Vorschläge gespannt.

```html
<!DOCTYPE html>
<html lang="de">
<head>
<meta charset="utf-8">
<title>Feinbissen – Teigtaschen mit Käsefülle</title>
<link href="https://fonts.googleapis.com/css2?family=Cinzel:wght@500;600&family=Montserrat:wght@400;500&family=Roboto+Condensed:wght@300;400;700&display=swap" rel="stylesheet">
<style>
  :root{
    --bg:#dcdcde;
    --bg-top:#a6a6a8;
    --label:#000000;
    --gold:#c9a25c;
    --gold-light:#e8c884;
    --gold-band:#e2bd72;
    --white:#ffffff;
    --board:#d9b88a;
    --board-light:#ecd6b4;
    --photo-dark:#1c1a18;
    --photo-mid:#3a332b;
    --ink:#1e1a16;
    --green:#2f6b2a;
  }
  *{box-sizing:border-box;margin:0;padding:0}
  html,body{width:1173px;height:1200px;overflow:hidden}
  body{
    position:relative;
    background:linear-gradient(180deg,var(--bg-top) 0%,#c9c9cb 35%,var(--bg) 55%,var(--bg) 100%);
    font-family:"Roboto Condensed",sans-serif;
    color:var(--white);
  }

  /* Brand lockup */
  .brand-lockup{position:absolute;left:443px;top:54px;width:295px;text-align:center}
  .maker-band{
    height:31px;background:linear-gradient(90deg,#e6c47c,var(--gold-band),#f0d49a);
    display:flex;align-items:center;justify-content:center;gap:14px;
    font-family:"Montserrat",sans-serif;font-size:13.5px;letter-spacing:5px;color:var(--white);
  }
  .maker-band .rule{width:28px;height:1px;background:var(--white)}
  .brand-name{
    margin-top:30px;display:flex;align-items:center;justify-content:center;gap:14px;
    font-family:"Roboto Condensed",sans-serif;font-weight:400;font-size:46px;color:var(--white);
  }
  .brand-name .dot{width:30px;height:30px;border-radius:50%;background:var(--green)}
  .brand-tagline{font-size:17px;font-weight:300;color:var(--white);margin-top:2px;letter-spacing:.5px}

  /* Crop marks */
  .crop{position:absolute;top:443px;width:1px;height:317px;background:#6e6e70}
  .crop.left{left:158px}.crop.right{left:1049px}

  /* Label */
  .label{position:absolute;left:91px;top:455px;width:1025px;height:293px;background:var(--label);overflow:hidden}
  .gold-rule{position:absolute;height:1px;background:var(--gold)}

  .section-title{position:absolute;font-family:"Cinzel",serif;font-weight:500;font-size:13.5px;color:var(--gold);letter-spacing:.3px}
  .small-head{position:absolute;font-weight:700;font-size:7.5px;letter-spacing:1.4px}
  .body-text{position:absolute;font-weight:300;font-size:9px;line-height:13.7px;color:var(--white)}
  .body-text b{font-weight:700}

  .ingredients{left:104px;top:55px;width:215px}
  .ingredients .row{display:flex}
  .ingredients .key{width:45px;flex:none}
  .prep{left:104px;top:124px;width:196px;text-align:justify}
  .storage{left:104px;top:243px;width:200px}

  /* Front panel */
  .front{position:absolute;left:331px;top:0;width:407px;height:293px}
  .front-photo{position:absolute;inset:0;
    background:radial-gradient(circle at 50% 50%,#8a8378 0%,var(--photo-mid) 45%,var(--photo-dark) 80%)}
  .board{position:absolute;left:80px;top:41px;width:216px;height:216px;border-radius:50%;
    background:radial-gradient(circle,var(--board-light) 0%,var(--board) 75%,#c39e6c 100%);
    box-shadow:0 0 0 3px rgba(255,255,255,.55)}
  .front-maker{position:absolute;left:125px;top:18px;width:122px;height:12px;background:var(--gold-band);
    display:flex;align-items:center;justify-content:center;gap:5px;
    font-family:"Montserrat",sans-serif;font-size:5.6px;letter-spacing:2px;color:var(--white)}
  .front-maker .rule{width:12px;height:.6px;background:var(--white)}
  .front-brand{position:absolute;left:128px;top:37px;width:120px;display:flex;align-items:center;gap:5px;
    font-size:15px;color:var(--white)}
  .front-brand .dot{width:11px;height:11px;border-radius:50%;background:var(--green);flex:none}
  .front-brand small{display:block;font-size:6px;font-weight:300;margin-top:-2px}
  .product-title{position:absolute;left:80px;top:70px;width:216px;text-align:center;
    font-family:"Cinzel",serif;font-weight:600;font-size:23px;line-height:20px;color:var(--ink)}
  .variety{position:absolute;left:143px;top:125px;width:91px;height:16px;border:1px solid var(--gold);background:var(--white);
    font-weight:700;font-size:7.5px;letter-spacing:1.3px;color:var(--ink);display:flex;align-items:center;justify-content:center}
  .claim{position:absolute;left:96px;top:150px;width:184px;text-align:center;font-weight:700;font-size:7.2px;line-height:9.5px;color:var(--ink)}
  .cheese-photo{position:absolute;left:108px;top:175px;width:159px;height:56px;border-radius:0 0 80px 80px;
    background:linear-gradient(160deg,#e9dfc4,#c9b585 55%,#8f8a6a)}
  .front-count{position:absolute;left:0;top:253px;width:100%;text-align:center;color:var(--gold-light);font-size:11.5px;line-height:15px}
  .front-count b{font-weight:700}

  /* Right panel */
  .free-from{position:absolute;left:793px;top:38px;font-weight:700;font-size:7.2px;line-height:10.5px}
  .short-rule{position:absolute;left:846px;top:79px;width:31px;height:1px;background:var(--gold)}
  .nutrition{position:absolute;left:794px;top:88px;width:130px}
  .nutrition h3{font-weight:700;font-size:6.5px;letter-spacing:1.2px;margin-bottom:3px}
  .nutrition table{border-collapse:collapse;font-weight:300;font-size:6px;width:100%}
  .nutrition td{height:9.4px;padding:0}
  .nutrition td.val{width:48px}
  .maker{position:absolute;left:794px;top:175px;width:150px}
  .maker h3{font-weight:700;font-size:6.5px;letter-spacing:1.2px;margin-bottom:4px}
  .maker p{font-weight:300;font-size:5.8px;line-height:9.5px}
  .maker .web{font-weight:700;font-size:6.5px;letter-spacing:.8px;margin-top:2px}
  .contents{position:absolute;left:794px;top:225px;font-weight:300;font-size:8.5px;line-height:10.5px}
  .contents b{font-weight:700}
  .contents .weight{font-weight:700;font-size:13px;line-height:17px}
  .code-field{position:absolute;left:854px;top:227px;width:84px;height:46px;background:var(--white)}
</style>
</head>
<body>
  <header class="brand-lockup">
    <div class="maker-band"><span class="rule"></span>WALTRUD KOH<span class="rule"></span></div>
    <div class="brand-name"><span class="dot"></span>feinbissen</div>
    <div class="brand-tagline">Teigtaschen handgemacht</div>
  </header>

  <span class="crop left"></span>
  <span class="crop right"></span>

  <main class="label">
    <span class="gold-rule" style="left:88px;top:19px;width:354px"></span>
    <span class="gold-rule" style="left:593px;top:19px;width:348px"></span>
    <span class="gold-rule" style="left:89px;top:279px;width:396px"></span>
    <span class="gold-rule" style="left:545px;top:279px;width:394px"></span>

    <h2 class="section-title" style="left:104px;top:33px">ZUTATEN</h2>
    <div class="body-text ingredients">
      <div class="row"><span class="key">TEIG (50%):</span><span>Dinkelmehl, Hartweizengriess, Eier, Olivenöl</span></div>
      <div class="row"><span class="key">FÜLLE (50%):</span><span>Käsemischung (Greyerzer, Emmentaler, Ricotta, Parmesan), Basilikum, Pfeffer, Meersalz</span></div>
    </div>

    <h2 class="section-title" style="left:104px;top:104px">ZUBEREITUNG</h2>
    <p class="body-text prep">Großen Topf mit <b>Salzwasser</b> zum Sieden bringen. Die gefrorenen Teigtaschen vorsichtig einlegen, Hitze reduzieren, behutsam mit dem Holzlöffel einige Male umrühren und max. <b>8 Minuten</b> auf kleiner Stufe leicht kochen lassen. Teigtaschen vorsichtig mit dem Holzlöffel aus dem Wasser nehmen und mit dem entsprechenden Guss anrichten.</p>

    <h3 class="small-head" style="left:104px;top:230px">AUFBEWAHRUNGSHINWEIS</h3>
    <p class="body-text storage">Im Tiefkühlfach *** bei -18° Celsius mindestens haltbar bis siehe Etikette auf der Rückseite.</p>

    <section class="front">
      <div class="front-photo" role="img" aria-label="Dunkler Holztisch mit Mehl, Weizenähren, Olivenöl, Ei und Nudelholz"></div>
      <div class="board"></div>
      <div class="front-maker"><span class="rule"></span>WALTRUD KOH<span class="rule"></span></div>
      <div class="front-brand"><span class="dot"></span><span>feinbissen<small>Teigtaschen handgemacht</small></span></div>
      <h1 class="product-title">TEIG-<br>TASCHEN</h1>
      <div class="variety">MIT KÄSEFÜLLE</div>
      <p class="claim">Handgemachte Teigtaschen gefüllt mit einem Mix aus Greyerzer, Emmentaler, Ricotta und Parmesan</p>
      <div class="cheese-photo" role="img" aria-label="Auswahl verschiedener Käsesorten mit Walnüssen"></div>
      <p class="front-count"><b>21 STÜCK</b> (3-4 Portionen)<br><b>630 g ℮</b></p>
    </section>

    <p class="free-from">Ohne Konservierungsstoffe<br>Ohne künstliche Aromen<br>Ohne Geschmacksverstärker</p>
    <span class="short-rule"></span>

    <section class="nutrition">
      <h3>DURCHSCHNITTLICHE NÄHRWERTE / 100g</h3>
      <table>
        <tr><td>Brennwert/Energie</td><td class="val">000 KJ/000 kcal</td></tr>
        <tr><td>Fett</td><td class="val">00 g</td></tr>
        <tr><td>davon gesättigte Fettsäuren</td><td class="val">00g</td></tr>
        <tr><td>Kohlenhydrate</td><td class="val">00g</td></tr>
        <tr><td>Zucker</td><td class="val">00g</td></tr>
        <tr><td>Eiweiss</td><td class="val">00g</td></tr>
        <tr><td>Salz</td><td class="val">00g</td></tr>
      </table>
    </section>

    <section class="maker">
      <h3>HERSTELLER</h3>
      <p>Waltrud Koh · Am Lindenweg 4 · AT-6850 Kornau<br>T: +43 (0) 660 12 34 56 78 · Mail: waltrudkoh@postnetz.at</p>
      <p class="web">www.feinbissen.at</p>
    </section>

    <p class="contents">INHALT<br><b>21 STÜCK</b><br>(3-4 Portionen)<br><span class="weight">630 g ℮</span></p>
    <div class="code-field"></div>
  </main>
</body>
</html>
```